Emerging Australian photographer

I'm based in Cunderdin, a small rural town in the Wheatbelt area of Western Australia. So its a good thing that I love to travel further afield both for pleasure and for work. To me that is one and the same thing in any event!

My desire is to take photos that make the viewers heart skip. I love taking photos of people doing the things they love or being with the people they love. For me, the joy of photography comes with capturing the 'moments between the moments'. I like candid photography best of all - like when the new husband is staring joyfully at his bride and at that minute is unaware of the photographer capturing the moment.

I am available for weddings, engagements, birthdays, special events, newborns, family or individual portraits. By the end of the year I will be accredited with the Coastal Guild of Image Artisans.

I need a card that stands out but is elegant and would sit well on the table at a wedding or be given out in the church grounds. Classy and a little bit sassy.

Target Market(s)

Consumers who are seeking photographic services, eg wedding guests who see me at work and make enquiries.

Industry/Entity Type

Church

Contact Information for Business Card

Tamsin Bexley Photography
Tamsin Bexley
0452 307 618
www.tamsinbexley.com.au
photos@tamsinbexley.com.au

Requirements
Must have
• Must fit with the theme in the watermarks, but be crisp and modern.
Nice to have
• However it's not essential to have the pink! Facebook and Twitter logos.
Should not have
• Old style fonts like times new roman.

```html
<!DOCTYPE html>
<html lang="en">
<head>
<meta charset="utf-8">
<title>Tamsin Bexley Photography – Business Card</title>
<link rel="stylesheet" href="https://fonts.googleapis.com/css2?family=Handlee&display=swap">
<style>
  :root {
    --page-bg: #ffffff;
    --pink-deep: #f294c0;
    --pink-mid: #f6b6d3;
    --pink-pale: #fce6ef;
    --wave: #e6c5d4;
    --mark-light: #8a8a8a;
    --mark-dark: #2a2a2a;
    --type-fill: #6f6f6a;
    --type-edge: #2e2e2b;
  }
  html, body {
    margin: 0;
    padding: 0;
    width: 1200px;
    height: 741px;
    overflow: hidden;
    background: var(--page-bg);
  }
  .card {
    display: block;
    width: 1200px;
    height: 741px;
  }
  .card__bg-start { stop-color: var(--pink-deep); }
  .card__bg-mid { stop-color: var(--pink-mid); }
  .card__bg-end { stop-color: var(--pink-pale); }
  .mark__light { stop-color: var(--mark-light); }
  .mark__dark { stop-color: var(--mark-dark); }
  .card__wave { fill: var(--wave); }
  .card__name {
    font-family: "Handlee", cursive;
    font-size: 64px;
    fill: var(--type-fill);
    stroke: var(--type-edge);
    stroke-width: 1.5px;
    paint-order: stroke;
  }
</style>
</head>
<body>
<svg class="card" viewBox="0 0 1200 741" xmlns="http://www.w3.org/2000/svg">
  <defs>
    <linearGradient id="cardBg" x1="0" y1="0" x2="1" y2="0.75">
      <stop offset="0" class="card__bg-start"/>
      <stop offset="0.5" class="card__bg-mid"/>
      <stop offset="1" class="card__bg-end"/>
    </linearGradient>
    <radialGradient id="markFill" cx="0.5" cy="0.5" r="0.5">
      <stop offset="0" class="mark__light"/>
      <stop offset="1" class="mark__dark"/>
    </radialGradient>
  </defs>

  <rect class="card__panel" x="44" y="47" width="1118" height="650" fill="url(#cardBg)"/>

  <circle class="card__illustration" role="img" aria-label="Camera lens illustration"
          cx="603" cy="356" r="244" fill="url(#markFill)"/>

  <path class="card__wave"
        d="M44,664 C120,570 200,526 272,524 C350,522 390,535 435,533 C520,530 560,525 609,511 C700,485 780,440 849,403 C960,340 1060,262 1162,245 L1162,697 L44,697 Z"/>

  <text class="card__name" x="117" y="632" textLength="987" lengthAdjust="spacingAndGlyphs">Tamsin Bexley Photography</text>
</svg>
</body>
</html>
```